Newspaper Ad for Cool Hawaiian PPE Company

We need an incredible ad for our local newspaper to tell everyone about BreezeGuard.com. We want a beautiful ad that is sophisticated with a local flair. Less is more. Clean. Stands out. We are safely shipping masks and PPE to our local community. Everyone has access to the supplies they need to keep them and their loved ones safe during the pandemic. Make it really pop.

Target Market(s)

Community members

Requirements
Must have
• Half Page:

Specs 9.7” x 10” column inches for the half page. Minimum 300 dpi, jpeg is fine.

```html
<!DOCTYPE html>
<html lang="en">
<head>
<meta charset="utf-8">
<title>BreezeGuard.com – Half Page Newspaper Ad</title>
<link rel="stylesheet" href="https://fonts.googleapis.com/css2?family=Montserrat:wght@300;400;500;800&display=swap">
<style>
  :root {
    --page-bg: #e4e4e2;
    --paper: #f4f4f2;
    --navy-deep: #1b2f4c;
    --navy-mid: #4a5f7a;
    --slate-light: #b4c0cc;
    --green: #138a3a;
    --green-soft: rgba(22, 150, 62, 0.78);
    --white: #ffffff;
    --photo-warm: #c7a994;
    --photo-cool: #8fa2a8;
  }
  html, body {
    margin: 0;
    width: 1200px;
    height: 933px;
    overflow: hidden;
    background: var(--page-bg);
    font-family: "Montserrat", sans-serif;
  }
  .ad {
    position: absolute;
    left: 160px;
    top: 16px;
    width: 880px;
    height: 900px;
    background: var(--paper);
    overflow: hidden;
  }
  .ad-shapes { position: absolute; inset: 0; }
  .brand {
    position: absolute;
    left: 64px;
    top: 84px;
    display: flex;
    align-items: center;
    gap: 12px;
    color: var(--white);
    font-size: 30px;
    font-weight: 500;
    letter-spacing: 0.2px;
  }
  .brand-mark {
    width: 14px;
    height: 14px;
    background: var(--green);
  }
  .headline {
    position: absolute;
    left: 64px;
    top: 360px;
    margin: 0;
    color: var(--white);
    font-size: 36px;
    font-weight: 800;
    line-height: 1.18;
    letter-spacing: 1.5px;
    text-transform: uppercase;
  }
  .tagline {
    position: absolute;
    left: 64px;
    top: 508px;
    width: 440px;
    margin: 0;
    color: var(--white);
    font-size: 19px;
    font-weight: 300;
    line-height: 1.35;
  }
  .contact {
    position: absolute;
    left: 64px;
    display: flex;
    align-items: flex-start;
    gap: 14px;
    color: var(--white);
    font-size: 17px;
    font-weight: 300;
    line-height: 1.35;
  }
  .contact-address { top: 700px; }
  .contact-email { top: 790px; }
  .contact-icon {
    flex: none;
    width: 30px;
    height: 30px;
    border-radius: 50%;
    background: var(--green);
    display: flex;
    align-items: center;
    justify-content: center;
  }
  .social {
    position: absolute;
    right: 40px;
    bottom: 34px;
    display: flex;
    align-items: center;
    gap: 10px;
    color: var(--white);
    font-size: 20px;
    font-weight: 500;
  }
  .social-label { font-size: 12px; font-weight: 500; display: block; }
  .social-mark {
    width: 26px;
    height: 26px;
    background: var(--navy-deep);
  }
</style>
</head>
<body>
  <main class="ad">
    <svg class="ad-shapes" width="880" height="900" viewBox="0 0 880 900" aria-hidden="false">
      <defs>
        <linearGradient id="panelGradient" x1="0" y1="0" x2="0.35" y2="1">
          <stop offset="0" stop-color="#b4c0cc"/>
          <stop offset="0.45" stop-color="#4a5f7a"/>
          <stop offset="1" stop-color="#1b2f4c"/>
        </linearGradient>
        <linearGradient id="photoGradient" x1="0" y1="0" x2="1" y2="1">
          <stop offset="0" stop-color="#8fa2a8"/>
          <stop offset="0.35" stop-color="#b99a86"/>
          <stop offset="0.7" stop-color="#c7a994"/>
          <stop offset="1" stop-color="#a4566a"/>
        </linearGradient>
      </defs>
      <g role="img" aria-label="Photo of a smiling child wearing a patterned face mask at an outdoor market">
        <polygon points="470,230 880,180 880,900 600,900" fill="url(#photoGradient)"/>
      </g>
      <polygon class="dark-panel" points="0,0 300,0 640,900 0,900" fill="url(#panelGradient)"/>
      <polygon class="green-wedge" points="300,260 560,200 700,900 560,900" fill="var(--green-soft)"/>
      <polygon class="green-corner" points="540,820 880,690 880,900 520,900" fill="var(--green)"/>
      <rect class="green-square" x="540" y="740" width="40" height="40" fill="var(--green)" transform="rotate(-12 560 760)"/>
    </svg>

    <div class="brand"><span class="brand-mark"></span>BreezeGuard.com</div>

    <h1 class="headline">Personal Protective<br>Equipment for Family<br>&amp; Business</h1>
    <p class="tagline">We help supply the community products like face masks, gloves, infrared thermometers, and hand sanitizer</p>

    <div class="contact contact-address">
      <span class="contact-icon">
        <svg width="14" height="18" viewBox="0 0 14 18"><path d="M7 0C3.1 0 0 3.1 0 7c0 5 7 11 7 11s7-6 7-11c0-3.9-3.1-7-7-7zm0 9.5A2.5 2.5 0 1 1 7 4.5a2.5 2.5 0 0 1 0 5z" fill="#fff"/></svg>
      </span>
      <span>480 Lanai Palm Avenue<br>Honolulu, HI 96815</span>
    </div>

    <div class="contact contact-email">
      <span class="contact-icon">
        <svg width="16" height="12" viewBox="0 0 16 12"><rect x="0.5" y="0.5" width="15" height="11" fill="none" stroke="#fff"/><polyline points="0.5,0.5 8,7 15.5,0.5" fill="none" stroke="#fff"/></svg>
      </span>
      <span>info@breezeguard.com</span>
    </div>

    <div class="social">
      <span><span class="social-label">Find us on:</span>SocialHub</span>
      <span class="social-mark"></span>
    </div>
  </main>
</body>
</html>
```